Maren Spacial\floral Decorator

Maren is a spacial\floral decorator. She is passionate about Art, Life, Architecture, Painting, Music and movement. Her website will be used to showcase her spacial and floral design projects.
We are looking for a very unique website that stands apart from the crowd.
We believe that is achieved through simple high quality design Simple being very important.
The Home page should display primarily photos.
Your task is to provide an un-coded homepage template.
The page must be dynamic in its style and feel.

Maren has suggest a grid pattern for the images, similar to this http://www.dovelmarchblooms.co.uk. Overall We like the look and feel of this site.

We like the following color palettes, please base your design around one of them;
https://tintvault.example.com/#themes/search?term=5519047
https://tintvault.example.com/#themes/search?term=5513628
https://tintvault.example.com/#themes/search?term=5527154
https://tintvault.example.com/#themes/search?term=5518462
https://tintvault.example.com/#themes/search?term=5514309

Our target Market is High End Corporate Clients, located in Shanghai and Taipai. For these clients she utilise her floral and interior design skills to decorate a space. See Photos 2, 3 and 21 for examples.
She also targets High End personal clients for events such as weddings and gift combination i.e. flowers and something else.

Industry/Entity Type

Floral

Requirements
Must have
• Chinese/ English Language Selection
A selection of pictures that appear and disappear.
A menu system that includes:
Home – Portfolio – About Maren – Blog – Contact Her
A very subtle menu system linking to chatterbox, workbridge Up, q* and zhuta.
Nice to have
• We also like the use of an image for the background but this is not necessary.
Should not have
• Alot of Text, yes we now this isn't great for SEO but we will deal with that on other pages

```html
<!DOCTYPE html>
<html lang="en">
<head>
<meta charset="utf-8">
<title>Maren – Home</title>
<link href="https://fonts.googleapis.com/css2?family=Questrial&family=Damion&display=swap" rel="stylesheet">
<style>
:root{
  --purple:#3d3558;
  --purple-soft:#5a5178;
  --sage:#8db59f;
  --sage-deep:#7a9a88;
  --sage-text:#8fb39e;
  --ink:#3a3a3a;
  --muted:#5c5c5c;
  --page:#ffffff;
  --side:#cfcfcf;
  --rule:#dcdcdc;
}
*{margin:0;padding:0;box-sizing:border-box}
html,body{width:1200px;height:1062px;overflow:hidden}
body{
  position:relative;
  font-family:"Questrial",Arial,sans-serif;
  color:var(--ink);
  background:var(--side);
}
.side-photos{
  position:absolute;top:0;height:1062px;width:100px;
  background:linear-gradient(180deg,#d8d8d8 0%,#bdbdbd 35%,#d4d4d4 60%,#b5b5b5 100%);
}
.side-photos.left{left:0}
.side-photos.right{right:0;background:linear-gradient(180deg,#cfcfcf 0%,#e2e2e2 30%,#bcbcbc 65%,#d0d0d0 100%)}
.page{position:absolute;left:100px;top:0;width:1000px;height:1062px;background:var(--page)}
.main-nav{position:absolute;left:21px;top:22px;display:flex;gap:24px;font-size:13.5px}
.main-nav a{color:#333;text-decoration:none}
.contact-bar{position:absolute;right:22px;top:21px;display:flex;align-items:center;gap:10px;font-size:16px;color:var(--purple)}
.contact-bar .phone{display:flex;align-items:center;gap:6px;padding-right:12px;border-right:1px solid #ccc;height:26px}
.social{display:flex;gap:8px;font-size:10px;color:#777}
.social a{color:#777;text-decoration:none}
.top-band{position:absolute;left:0;top:60px;width:1000px;height:10px;background:linear-gradient(180deg,var(--purple) 0 5px,var(--sage) 5px 10px)}
.hero{position:absolute;left:0;top:70px;width:1000px;height:505px}
.hero-photo{position:absolute;inset:0;background:linear-gradient(135deg,#3b2a1c 0%,#6b4a2f 40%,#8c6a4a 60%,#4a3a2c 100%)}
.hero svg{position:absolute;left:0;top:0}
.dots{position:absolute;left:522px;top:479px;display:flex;gap:8px}
.dots i{width:11px;height:11px;border-radius:50%;background:#222;border:1px solid #555}
.badge{position:absolute;left:449px;top:-30px;width:166px;height:172px;border-radius:50%;background:#fff;border-bottom:3px solid var(--purple);box-shadow:0 3px 0 var(--sage);display:flex;align-items:flex-end;justify-content:center;padding-bottom:42px}
.badge-name{font-family:"Questrial",sans-serif;font-size:36px;color:var(--purple)}
.welcome{position:absolute;left:38px;top:596px}
.script{font-family:"Damion",cursive;color:var(--purple);font-weight:400}
.welcome h1{font-size:32px;line-height:32px}
.welcome p{font-size:22px;color:var(--sage-text);margin-top:2px}
.welcome-divider{position:absolute;left:301px;top:607px;width:1px;height:65px;background:var(--rule)}
.intro{position:absolute;left:329px;top:607px;width:645px;font-size:13.5px;line-height:16px;color:var(--muted)}
.intro a{color:var(--purple);text-decoration:none;font-weight:bold;margin-left:4px}
.section-rule{position:absolute;left:30px;top:685px;width:940px;height:2px;background:linear-gradient(90deg,transparent,#d8d8d8 20%,#d8d8d8 80%,transparent)}
.newsletter{position:absolute;left:40px;top:712px;width:374px}
.newsletter h2{font-size:32px;line-height:36px;padding-bottom:8px;border-bottom:1px dotted #bbb;width:310px}
.newsletter p{font-size:14px;line-height:20px;color:var(--muted);margin-top:22px}
.field{display:flex;align-items:center;margin-top:12px}
.field.first{margin-top:16px}
.field label{width:92px;font-size:14px;color:var(--muted)}
.field input{width:282px;height:29px;border:1px solid #ddd;box-shadow:inset 0 2px 3px #eee}
.signup{display:block;margin:14px 0 0 304px;width:70px;height:23px;background:var(--purple);color:#fff;border:none;border-radius:3px;font-family:inherit;font-size:12px;font-weight:bold}
.portfolio-photo{position:absolute;left:624px;top:714px;width:350px;height:219px;border:2px solid var(--purple-soft);background:linear-gradient(120deg,#5a4632,#3a2f26 45%,#6d7a5a 75%,#2f2a24)}
.portfolio-circle{position:absolute;left:453px;top:705px;width:248px;height:248px;border-radius:50%;background:radial-gradient(circle at 40% 40%,#86a694,var(--sage-deep));color:#fff;padding:58px 0 0 44px}
.portfolio-circle .script{color:#fff;font-size:34px;line-height:26px}
.portfolio-circle h3{font-weight:400;font-size:25px;line-height:24px}
.portfolio-circle p{font-size:12px;line-height:16px;margin-top:4px;width:180px}
.portfolio-circle a{display:block;font-size:9px;color:#fff;text-decoration:none;margin-top:14px;letter-spacing:.5px}
.site-footer{position:absolute;left:0;top:993px;width:1000px;height:69px;background:linear-gradient(180deg,#e9e9e9,#f6f6f6 40%,#ececec);border-top:1px solid #e0e0e0;text-align:center;font-size:12px;color:#777}
.footer-nav{margin-top:16px}
.footer-nav a{color:#777;text-decoration:none;margin:0 6px}
.copyright{margin-top:6px}
</style>
</head>
<body>
<div class="side-photos left" role="img" aria-label="Faded grey photos of floral decorations"></div>
<div class="side-photos right" role="img" aria-label="Faded grey photos of floral table settings"></div>
<div class="page">
  <nav class="main-nav">
    <a href="#">Home</a><a href="#">Portfolio</a><a href="#">About Maren</a><a href="#">Blog</a><a href="#">Contact Her</a>
  </nav>
  <div class="contact-bar">
    <span class="phone">
      <svg width="13" height="16" viewBox="0 0 13 16"><path d="M3 1 L5.5 1 L6 5 L4.3 6 Q5.5 9.5 8 11 L9.2 9.5 L12.5 10.5 L12 14 Q11 15.5 8 14 Q2 10 1.5 3.5 Q1.5 1.5 3 1Z" fill="#3d3558"/></svg>
      0400 5512 874
    </span>
    <span class="social"><a href="#">chatterbox</a><a href="#">q*</a><a href="#">workbridge Up</a><a href="#">zhuta</a></span>
  </div>
  <div class="top-band"></div>
  <div class="hero">
    <div class="hero-photo" role="img" aria-label="Interior decorated with roses, greenery and a wooden serving table"></div>
    <svg width="1000" height="505" viewBox="0 0 1000 505">
      <path d="M0 478 Q500 530 1000 478 L1000 505 L0 505Z" fill="#fff"/>
      <path d="M0 478 Q500 530 1000 478 L1000 484 Q500 536 0 484Z" fill="#8db59f"/>
      <path d="M0 484 Q500 536 1000 484 L1000 492 Q500 544 0 492Z" fill="#3d3558"/>
    </svg>
    <div class="dots"><i></i><i></i><i></i><i></i></div>
  </div>
  <div class="badge"><span class="badge-name">Maren</span></div>

  <section class="welcome">
    <h1 class="script">Welcome</h1>
    <p>to our decorative world</p>
  </section>
  <div class="welcome-divider"></div>
  <p class="intro">Vestibulum ac arcu et tortor porta egestas quis id nisi. Fusce eu mi nisl, non gravida massa. Donec malesuada ultricies enim ac scelerisque. Maecenas pretium tincidunt quam, id. Praesent ultricies facili sis lorem ac mollis. <a href="#">Learn more...</a></p>
  <div class="section-rule"></div>

  <section class="newsletter">
    <h2 class="script">Sigup Newsletter</h2>
    <p>Donec faucibus malesuada eleifend. Phasellus vulputa te faucibus lobortis.</p>
    <div class="field first"><label>Your Name</label><input type="text"></div>
    <div class="field"><label>Your Email</label><input type="text"></div>
    <button class="signup">Sign Up</button>
  </section>

  <div class="portfolio-photo" role="img" aria-label="Lounge with leather chairs, flowers and glassware"></div>
  <div class="portfolio-circle">
    <div class="script">portfolio</div>
    <h3>view my latest<br>decorations</h3>
    <p>Sed non mi neque. Cras et ligula nunc, eu blandit mauris.</p>
    <a href="#">VIEW MORE</a>
  </div>

  <footer class="site-footer">
    <div class="footer-nav"><a href="#">Home</a> | <a href="#">Portfolio</a> | <a href="#">About Maren</a> | <a href="#">Blog</a> | <a href="#">Contact Her</a></div>
    <div class="copyright">Copyrights All Rights Reserved</div>
  </footer>
</div>
</body>
</html>
```